New Podcast focussing on non-mainstream interventions for guidance needs podcast art

I need an exquisite piece of podcast art work for the launch of my new podcast 'Beyond the Still'. This podcast explores unorthodox, esoteric and unconventional methods to find peace, clarity and direction in life. Topics include family Constellations Systems, Psychedelics, Equine Therapy and Floatation to name a few. A teaser has been posted on Talvora with a strong response. The audience is primarily midlifers or those in a career/personal crisis of direction. It's meant to comfort, inform and empower and offer other ways rather than mainstream to work out what to do with your life. The file shared with you shows the pic used on Talvora as it's illustrating the idea of illumination. You can use it or not, and whilst I am ex-Military, I don't want the cover to convey an overly military influence. I'd like 'Beyond the Still' to feature on the art work and my name, Mirela Dunford. I'd like inspiration, creativity, and the idea of hope conveyed as well as clarity and courage. Whilst the podcast is about finding your direction please do no use compass images or cross road images as that is too obvious.
Hope that all helps. Looking forward to your ideas.

```html
<!DOCTYPE html>
<html lang="en">
<head>
<meta charset="utf-8">
<title>Beyond the Still – podcast cover</title>
<link rel="stylesheet" href="https://fonts.googleapis.com/css2?family=Jost:wght@300;500;700&display=swap">
<style>
  :root {
    --page-bg: #f3fdf1;
    --cover-orange: #c57a0f;
    --line-rust: #b3600b;
    --fan-deep: #b86c0c;
    --type-cream: #f3fcef;
    --shadow-rust: rgba(150, 70, 5, 0.75);
    --accent-green: #76e87a;
  }

  html, body {
    margin: 0;
    padding: 0;
    width: 1200px;
    height: 1000px;
    overflow: hidden;
    background: var(--page-bg);
  }

  .cover {
    position: absolute;
    left: 280px;
    top: 180px;
    width: 640px;
    height: 640px;
    background: var(--cover-orange);
    overflow: hidden;
    font-family: "Jost", "Futura", sans-serif;
    color: var(--type-cream);
  }

  .cover__linework {
    position: absolute;
    inset: 0;
    width: 640px;
    height: 640px;
  }

  .cover__fan-illustration {
    position: absolute;
    left: 96px;
    top: 22px;
    width: 450px;
    height: 445px;
    border-radius: 50% 50% 38% 38% / 60% 60% 40% 40%;
    background: radial-gradient(ellipse at 50% 70%, var(--fan-deep) 0%, rgba(184, 108, 12, 0.55) 55%, rgba(197, 122, 15, 0) 75%);
  }

  .title {
    margin: 0;
    font-weight: 700;
  }

  .title__line {
    position: absolute;
    display: block;
    line-height: 1;
    white-space: nowrap;
  }

  .title__line--top {
    left: 54px;
    top: 40px;
    font-size: 60px;
    letter-spacing: 0.5px;
  }

  .title__line--joiner {
    left: 102px;
    top: 290px;
    font-size: 52px;
    font-weight: 500;
  }

  .title__line--hero {
    left: 100px;
    top: 331px;
    font-size: 176px;
    letter-spacing: 0;
    text-shadow: 6px 6px 6px var(--shadow-rust);
  }

  .host-name {
    position: absolute;
    left: 0;
    right: 0;
    top: 564px;
    margin: 0;
    text-align: center;
    font-size: 26px;
    font-weight: 300;
    letter-spacing: 1px;
    line-height: 1;
  }
</style>
</head>
<body>
  <main class="cover">
    <div class="cover__fan-illustration" role="img" aria-label="Line illustration of a peacock with its tail fanned open behind the title"></div>

    <svg class="cover__linework" viewBox="0 0 1101 1101" aria-hidden="true">
      <g fill="none" stroke="var(--line-rust)" stroke-width="7" stroke-linecap="round">
        <path class="linework__arc" d="M815 126 Q955 128 975 279"/>
        <path class="linework__frame" d="M864 0 V135 Q878 262 975 279 Q1000 288 1050 288 H1101"/>
        <path class="linework__rule" d="M975 279 V975"/>
        <path class="linework__corner-curve" d="M0 900 Q40 918 80 952"/>
        <path class="linework__corner-curve" d="M135 1006 Q172 1050 195 1101"/>
      </g>
      <g fill="var(--accent-green)">
        <circle class="linework__dot" cx="777" cy="126" r="23"/>
        <circle class="linework__dot" cx="107" cy="978" r="23"/>
      </g>
    </svg>

    <h1 class="title">
      <span class="title__line title__line--top">BEYOND</span>
      <span class="title__line title__line--joiner">the</span>
      <span class="title__line title__line--hero">STILL</span>
    </h1>

    <p class="host-name">MIRELA DUNFORD</p>
  </main>
</body>
</html>
```